Private Gym Needs a Rack Card Design

We need a basic front and back rack card (same size as post card) that gives basic information about our brand, and includes our logo. Please see attached logo and required content below.

Target Market(s)

Upscale, private gym.

Industry/Entity Type

Gym

Font styles to use
Sans Serif

Colors
ffffff
5c5c5c
000000
dbdbdb
f78f20

Requirements
Must have
• Business Logo and the following text in a clean, modern, easy-to-read, artistic manner. Style and design must be clean, incorporate our color scheme of MOSTLY white, light grey, charcoal, with just pops of orange. We want the card itself to be mostly white background. Must include website URL as well: corevantagestudio.com
• FRONT CARD:
• Logo
• A safe and individualized approach to exercise
• Our method employs the latest weight resistance training exercises and coaching for healthy living. Not only is our workout methodology effective, it’s safe.
• Our Method…
• -Improves Functional Movement
• -Promotes Weight Loss
• -Builds Strength
• -Increases Flexibility 

• BACK:
• Change Your Body. Find Your Strength.
• There’s 40 years of success behind our proven method
• What is The Formwell? 
• The Formwell is all about teaching our clients how to lift weights and exercise with the proper technique. There’s no slinging or jerking at our gym; only controlled movements that yield real results.
• Come workout with us in our private gym. We are located in Durham adjacent to Harlow Campus and 5 minutes from downtown Durham.
• Address: 482 Linden Ave, Durham, NC 27705
• Phone: (919) 555-2741
• Hours: 9:00 AM – 9:00 PM
Nice to have
• Great organization of text, maybe some columns, colored bullet points, cool graphics and logos.
Should not have
• Busy or crowded design. All lines should be sleek, straight, and streamline. NO STOCK IMAGES, but logos are GREAT

```html
<!DOCTYPE html>
<html lang="en">
<head>
<meta charset="utf-8">
<title>The Formwell – Rack Card</title>
<link href="https://fonts.googleapis.com/css2?family=Open+Sans:wght@400;600;700&family=Roboto+Condensed:wght@400&family=Montserrat:wght@600&display=swap" rel="stylesheet">
<style>
  :root {
    --orange: #f26a35;
    --charcoal: #5c5c5c;
    --ink: #222222;
    --grey: #77777a;
    --rule: #a9a9ab;
    --light: #dbdbdb;
    --white: #ffffff;
    --stage: #ececec;
  }
  * { margin: 0; padding: 0; box-sizing: border-box; }
  html, body { width: 1200px; height: 830px; overflow: hidden; background: var(--stage); }
  body { position: relative; font-family: "Open Sans", sans-serif; color: var(--ink); }

  .card {
    position: absolute; top: 56px; width: 538px; height: 694px;
    background: var(--white);
    border-top: 10px solid var(--rule); border-bottom: 10px solid var(--rule);
    box-shadow: 0 6px 18px rgba(0,0,0,.18);
  }
  .card--front { left: 53px; }
  .card--back { left: 616px; }
  .abs { position: absolute; }
  .center { left: 0; right: 0; text-align: center; }
  .accent { color: var(--orange); }

  /* wordmark */
  .brand-name { top: 62px; font-size: 54px; font-weight: 700; color: var(--charcoal); letter-spacing: 1px; line-height: 1; }
  .brand-sub { top: 130px; font-size: 14px; font-weight: 700; color: var(--charcoal); letter-spacing: 6px; }

  .intro { font-size: 19px; line-height: 23.5px; text-transform: uppercase; }
  .intro--one { top: 186px; }
  .intro--two { top: 264px; }

  .benefit-icon {
    top: 335px; width: 74px; height: 74px; margin-left: -37px;
    border: 1.5px solid #9a9a9a; border-radius: 50%;
    display: flex; align-items: center; justify-content: center;
  }
  .benefit-icon span { width: 34px; height: 34px; border-radius: 50%; background: #8f8f8f; }
  .benefit {
    top: 436px; width: 110px; height: 126px;
    border-top: 6px solid var(--rule);
    display: flex; align-items: center; justify-content: center;
    background: linear-gradient(var(--white) 0 6px, var(--grey) 6px);
    padding-top: 6px;
    font-family: "Roboto Condensed", sans-serif; font-size: 17.5px; line-height: 22px;
    color: var(--white); text-align: center;
  }

  .band {
    left: 26px; width: 484px; height: 46px; background: var(--orange);
    color: var(--white); font-size: 17px; text-transform: uppercase;
    display: flex; align-items: center; justify-content: center;
    box-shadow: 0 6px 5px -3px rgba(0,0,0,.35);
  }
  .band--front { top: 582px; }
  .band--back { top: 52px; }
  .url { top: 644px; font-size: 15px; color: var(--grey); }

  /* back */
  .legacy { top: 114px; font-size: 17.5px; line-height: 21px; text-transform: uppercase; }
  .copy { font-size: 17.5px; line-height: 21.5px; }
  .copy b { font-weight: 600; color: var(--orange); }
  .copy--what { top: 197px; }
  .copy--visit { top: 267px; }
  .no-list { top: 380px; font-size: 17.5px; font-weight: 600; color: var(--orange); }
  .yield {
    top: 411px; left: 26px; width: 484px; height: 48px; background: var(--grey);
    color: var(--white); font-size: 24px; display: flex; align-items: center; justify-content: center;
  }
  .yield::after {
    content: ""; position: absolute; left: 50%; bottom: -8px; margin-left: -11px;
    border-left: 11px solid transparent; border-right: 11px solid transparent; border-top: 8px solid var(--grey);
  }
  .results { top: 470px; font-family: "Montserrat", sans-serif; font-weight: 600; font-size: 62px; letter-spacing: 3px; color: var(--charcoal); }

  .foot-brand { left: 38px; top: 600px; width: 175px; white-space: nowrap; }
  .foot-brand strong { display: block; font-size: 21px; font-weight: 700; color: var(--charcoal); line-height: 1; }
  .foot-brand small { display: block; margin-top: 7px; font-size: 7.5px; font-weight: 700; letter-spacing: 2.2px; color: var(--charcoal); }
  .contact { left: 234px; top: 592px; list-style: none; }
  .contact li { display: flex; align-items: center; gap: 10px; height: 24.5px; font-size: 16.5px; color: var(--charcoal); white-space: nowrap; }
  .contact svg { width: 16px; height: 16px; flex: none; }
</style>
</head>
<body>

<section class="card card--front">
  <div class="abs center brand-name">THE FORMWELL</div>
  <div class="abs center brand-sub">PRIVATE TRAINING STUDIO</div>

  <p class="abs center intro intro--one">The <span class="accent">Formwell</span> employs the latest weight<br>resistance training exercises and<br>coaching for healthy living.</p>
  <p class="abs center intro intro--two">Not only is our workout methodology<br>effective, <span class="accent">it’s safe</span></p>

  <div class="abs benefit-icon" style="left:82px" role="img" aria-label="Icon of a person lifting a dumbbell"><span></span></div>
  <div class="abs benefit-icon" style="left:206px" role="img" aria-label="Icon of a flexed arm"><span></span></div>
  <div class="abs benefit-icon" style="left:331px" role="img" aria-label="Icon of a person doing a sit-up"><span></span></div>
  <div class="abs benefit-icon" style="left:456px" role="img" aria-label="Icon of a bathroom scale"><span></span></div>

  <div class="abs benefit" style="left:25px">Improves<br>Functional<br>Movement</div>
  <div class="abs benefit" style="left:150px">Builds<br>Strength</div>
  <div class="abs benefit" style="left:275px">Increases<br>Flexibility</div>
  <div class="abs benefit" style="left:400px">Promotes<br>Weight Loss</div>

  <div class="abs band band--front">A safe &amp; individualized approach to exercise</div>
  <div class="abs center url">www.corevantagestudio.com</div>
</section>

<section class="card card--back">
  <div class="abs band band--back">Change your body. Find your strength</div>
  <p class="abs center legacy">There’s 40 years of success behind<br>the proven <span class="accent">Formwell</span></p>

  <p class="abs center copy copy--what"><b>What is The Formwell?</b> The Formwell is all about teaching<br>our clients how to lift weights and exercise<br>with the proper technique.</p>
  <p class="abs center copy copy--visit"><b>Come workout with us in our private gym.</b> We are<br>located in Durham adjacent to Harlow Campus and<br>5 min from downtown Durham.</p>

  <p class="abs center no-list">NO SLINGING · NO JERKING · NO TIME-WASTING</p>
  <div class="abs yield">Only Controlled Movements That Yield...</div>
  <div class="abs center results">REAL RESULTS</div>

  <div class="abs foot-brand">
    <strong>THE FORMWELL</strong>
    <small>PRIVATE TRAINING STUDIO</small>
  </div>
  <ul class="abs contact">
    <li><svg viewBox="0 0 16 16"><path d="M8 1a5 5 0 0 0-5 5c0 3.8 5 9 5 9s5-5.2 5-9a5 5 0 0 0-5-5z" fill="none" stroke="#f26a35" stroke-width="2"/><circle cx="8" cy="6" r="1.8" fill="#f26a35"/></svg>482 Linden Ave, Durham, NC 27705</li>
    <li><svg viewBox="0 0 16 16"><path d="M1 7c0-3 14-3 14 0v1.5h-3.5V7h-7v1.5H1z M4 9h8l2 5H2z" fill="#f26a35"/><circle cx="8" cy="11.5" r="1.4" fill="#fff"/></svg>(919) 555-2741</li>
    <li><svg viewBox="0 0 16 16"><circle cx="8" cy="8" r="6.5" fill="none" stroke="#f26a35" stroke-width="2"/><path d="M8 4.5V8h3" fill="none" stroke="#f26a35" stroke-width="1.8"/></svg>9:00 AM – 9:00 PM</li>
  </ul>
</section>

</body>
</html>
```